Olive Oil label for bottle 0.5l approx. 10x12 cm

I am running a Spa hotel in Bavaria (logo attached) and my family lives in Greece (Bavarian and Greek flag have the same colors). They produce organic olive oil first cold pressed extra virgin. I would need a label for 0,5 liter bottles to reach them out to my guests and they should see the high quality of the olive oil and the family connection Spa-hotel Bavaria to family in Greece. The name of the family is Morvatek, the hotel is called Tannegg, the olive oil comes from Greece/Argolis/Kranidi. The name of the small olive company is Kerano Hawks. There should be a space for the best before date and the organic control number (handwritten) . The hotel logo is not mandatory. Should look nice 😉

```html
<!DOCTYPE html>
<html lang="en">
<head>
<meta charset="utf-8">
<title>Kerano Hawks – Organic Extra Virgin Olive Oil Label</title>
<link rel="stylesheet" href="https://fonts.googleapis.com/css2?family=Cinzel:wght@400;600;700&family=Cormorant+SC:wght@400;500&family=Quicksand:wght@300;400;500;600&display=swap">
<style>
  :root {
    --page: #ffffff;
    --label-dark: #2a2b27;
    --label-dark-soft: #31332e;
    --panel-sand: #bcae9a;
    --panel-sand-soft: #b3a48f;
    --ink-dark: #2a2b27;
    --text-light: #f3eee6;
    --write-box: #ffffff;
    --flag-blue: #1b63b8;
  }
  * { margin: 0; padding: 0; box-sizing: border-box; }
  html, body {
    width: 1200px; height: 1200px; overflow: hidden;
    background: var(--page);
  }
  .canvas { position: relative; width: 1200px; height: 1200px; }

  .label {
    position: absolute; left: 120px; top: 67px;
    width: 960px; height: 1066px;
    background: radial-gradient(ellipse at 40% 50%, var(--label-dark-soft), var(--label-dark) 70%);
  }

  .front-panel {
    position: absolute; left: 287px; top: 68px;
    width: 377px; height: 928px;
    background: linear-gradient(170deg, var(--panel-sand) 0%, var(--panel-sand-soft) 55%, var(--panel-sand) 100%);
  }

  .brand {
    position: absolute; left: 0; top: 24px; width: 100%;
    display: flex; flex-direction: column; align-items: center;
    font-family: "Quicksand", sans-serif; color: var(--text-light);
  }
  .brand-family {
    font-size: 19px; font-weight: 400; letter-spacing: 0.5px; line-height: 1;
  }
  .brand-name {
    margin-top: 20px;
    font-size: 24px; font-weight: 400; line-height: 1;
  }
  .brand-tagline {
    margin-top: 3px;
    font-size: 8px; font-weight: 400; letter-spacing: 0.3px;
  }

  .product-title {
    position: absolute; left: 21px; top: 244px;
    color: var(--ink-dark);
  }
  .title-organic {
    font-family: "Quicksand", sans-serif; font-weight: 300;
    font-size: 36px; line-height: 1; color: var(--text-light);
  }
  .title-grade {
    font-family: "Cinzel", serif; font-weight: 600;
    font-size: 38px; line-height: 1; margin-top: 2px;
    color: var(--text-light); letter-spacing: 0.5px;
  }
  .title-product {
    font-family: "Cinzel", serif; font-weight: 700;
    font-size: 106px; line-height: 1.04; margin-top: 42px;
    letter-spacing: -1px; color: var(--ink-dark);
  }

  .product-details {
    position: absolute; left: 21px; top: 795px;
    color: var(--text-light);
  }
  .detail-process {
    font-family: "Cormorant SC", serif; font-weight: 400;
    font-size: 36px; line-height: 1;
  }
  .detail-origin {
    font-family: "Quicksand", sans-serif; font-weight: 500;
    font-size: 21px; line-height: 1.25; margin-top: 2px;
  }
  .detail-volume {
    font-family: "Quicksand", sans-serif; font-weight: 500;
    font-size: 20px; line-height: 1.25; margin-top: 32px;
  }

  .side-column {
    position: absolute; left: 768px; top: 0;
    width: 192px; height: 1066px;
  }
  .side-text {
    font-family: "Quicksand", sans-serif; fill: var(--text-light);
    font-weight: 500;
  }
</style>
</head>
<body>
<div class="canvas">
  <div class="label" role="img" aria-label="Dark label background with faint hand-drawn olive branches and fruit">
    <section class="front-panel" role="img" aria-label="Sand-coloured panel with faint olive branch and olive fruit drawing">
      <header class="brand">
        <div class="brand-family">Morvatek</div>
        <div class="brand-name">Kerano Hawks</div>
        <div class="brand-tagline">Familienöl vom Hof Kranidi</div>
      </header>

      <div class="product-title">
        <p class="title-organic">organic</p>
        <p class="title-grade">Extra Virgin</p>
        <h1 class="title-product">OLIVE<br>OIL</h1>
      </div>

      <div class="product-details">
        <p class="detail-process">First Cold Pressed</p>
        <p class="detail-origin">Origin: Greece/Argolis/Kranidi</p>
        <p class="detail-volume">500 ml | (16.90 fl oz</p>
      </div>
    </section>

    <svg class="side-column" viewBox="640 0 160 888" xmlns="http://www.w3.org/2000/svg">
      <rect class="write-box control-box" x="650" y="47" width="89" height="190" fill="var(--write-box)"/>
      <text class="side-text" transform="translate(687 365) rotate(-90)" font-size="24">Organic</text>
      <text class="side-text" transform="translate(724 365) rotate(-90)" font-size="24">Control #</text>

      <rect class="write-box date-box" x="650" y="372" width="89" height="155" fill="var(--write-box)"/>
      <text class="side-text" transform="translate(682 617) rotate(-90)" font-size="24">Best</text>
      <text class="side-text" transform="translate(706 617) rotate(-90)" font-size="24">Before</text>
      <text class="side-text" transform="translate(730 617) rotate(-90)" font-size="24">Date</text>

      <line x1="656" y1="629" x2="734" y2="629" stroke="var(--text-light)" stroke-width="2"/>

      <text class="side-text" transform="translate(684 822) rotate(-90)" font-size="13">100%</text>
      <text class="side-text" transform="translate(694 764) rotate(-90)" font-size="28">SOURCED</text>
      <text class="side-text" transform="translate(716 772) rotate(-90)" font-size="20">from Greece</text>

      <g class="greek-flag">
        <rect x="688" y="777" width="29" height="43" fill="var(--flag-blue)"/>
        <rect x="691" y="777" width="3" height="43" fill="#fff"/>
        <rect x="697" y="777" width="3" height="43" fill="#fff"/>
        <rect x="703" y="777" width="3" height="43" fill="#fff"/>
        <rect x="709" y="777" width="3" height="43" fill="#fff"/>
        <rect x="688" y="804" width="16" height="16" fill="var(--flag-blue)"/>
        <rect x="694.5" y="804" width="3" height="16" fill="#fff"/>
        <rect x="688" y="810.5" width="16" height="3" fill="#fff"/>
      </g>
    </svg>
  </div>
</div>
</body>
</html>
```